We Brambleton Grace Assembly Church Need a Post card that will be an invite for just one Sunday...which is THE LAST SUNDAY of the year. We are a small church but we are pushing to have 150 the last Sunday of 2014 which is December 28th 2014...Our service will begin at 10 a.m. We will have a meal to follow service. I would like for you to help me with a nice back ground that will grab peoples attention.. and also I like to keep the same theme and make some folding Business cards to send people thank you for visiting. and also a regular size business card to slip inside that and to hand out on a daily basis... Our Web site is www.Brambleton1stGraceAssembly.example all our info is on there and you can kind of see our theme we are going with. and also I was wondering is it possible to push the post Cards THE LAST SUNDAY CARD so we can start handing them out... we like to have 500 of those and say 1000 Folding business cards and 1000 regular Busyness cards..

Nmae . Pastor Dale Morrow, # 555-274-8160

Industry/Entity Type

Church

```html
<!DOCTYPE html>
<html lang="en">
<head>
<meta charset="utf-8">
<title>Brambleton Grace Assembly Church – Card Set</title>
<link href="https://fonts.googleapis.com/css2?family=Lato:wght@300;400&family=Courgette&display=swap" rel="stylesheet">
<style>
  :root {
    --backdrop: #a4a5a9;
    --silver-edge: #c9cacd;
    --silver-mid: #e6e7e9;
    --silver-shine: #fafafa;
    --church-blue: #1a85ad;
    --ink: #1e1e1e;
    --ink-soft: #4a4a4a;
    --white: #ffffff;
    --frost-light: #eef0f4;
    --frost-mid: #cfd3dc;
    --frost-deep: #9ea3ae;
    --card-shadow: 6px 8px 10px rgba(0, 0, 0, 0.28);
  }
  * { margin: 0; padding: 0; box-sizing: border-box; }
  html, body { width: 1200px; height: 804px; overflow: hidden; }
  body {
    position: relative;
    background: var(--backdrop);
    font-family: "Lato", Arial, sans-serif;
    color: var(--ink);
  }
  .card { position: absolute; overflow: hidden; box-shadow: var(--card-shadow); }
  .silver {
    background: linear-gradient(90deg, var(--silver-edge) 0%, var(--silver-mid) 35%, var(--silver-shine) 58%, var(--silver-mid) 78%, var(--silver-edge) 100%);
  }
  .center-name { text-align: center; font-weight: 300; line-height: 1.15; }

  /* Business card front */
  .card-front { left: 63px; top: 111px; width: 495px; height: 305px; display: flex; align-items: center; justify-content: center; }
  .card-front .center-name { color: var(--church-blue); font-size: 22px; }

  /* Business card back */
  .card-back { left: 63px; top: 431px; width: 495px; height: 304px; }
  .lockup { position: absolute; display: flex; align-items: center; gap: 10px; font-weight: 300; color: var(--ink-soft); }
  .lockup .dot { width: 14px; height: 14px; border-radius: 50%; background: var(--church-blue); flex: none; }
  .lockup .town { font-size: 31px; line-height: 1; letter-spacing: 0.5px; }
  .lockup .sub { font-size: 11px; letter-spacing: 0.3px; margin-top: 3px; }
  .card-back .lockup { left: 38px; top: 22px; }
  .pastor { position: absolute; left: 78px; top: 140px; font-size: 18px; }
  .divider { position: absolute; left: 247px; top: 114px; width: 1px; height: 103px; background: #8c8c8c; }
  .contacts { position: absolute; left: 268px; top: 124px; list-style: none; font-size: 12.5px; line-height: 1.15; color: var(--ink); }
  .contacts li { display: flex; gap: 6px; margin-bottom: 7px; }
  .contacts svg { width: 11px; height: 11px; flex: none; margin-top: 2px; fill: #8a8a8a; }
  .web-band { position: absolute; left: 0; bottom: 0; width: 100%; height: 41px; background: var(--church-blue); color: var(--white); font-size: 15.5px; letter-spacing: 0.3px; display: flex; align-items: center; justify-content: center; }

  /* Folding card cover */
  .card-cover { left: 637px; top: 31px; width: 521px; height: 355px; background: var(--church-blue); display: flex; align-items: center; justify-content: center; border-top: 2px solid var(--white); }
  .card-cover .center-name { color: var(--white); font-size: 26px; }

  /* Folding card inside */
  .card-inside { left: 637px; top: 406px; width: 521px; height: 356px; }
  .winter-photo { position: absolute; inset: 0; background: radial-gradient(ellipse at 40% 60%, var(--frost-light) 0%, var(--frost-mid) 60%, var(--frost-deep) 100%); }
  .thanks { position: absolute; left: 0; right: 0; top: 146px; text-align: center; font-family: "Courgette", cursive; font-size: 36px; color: #2c2c2c; }
  .card-inside .lockup { left: 28px; top: 286px; }
</style>
</head>
<body>

  <section class="card silver card-front" aria-label="Business card front">
    <p class="center-name">Brambleton<br>Grace Assembly Church</p>
  </section>

  <section class="card silver card-back" aria-label="Business card back">
    <div class="lockup">
      <span class="dot"></span>
      <div><div class="town">Brambleton</div><div class="sub">GRACE ASSEMBLY CHURCH</div></div>
    </div>
    <p class="pastor">Pastor Dale Morrow</p>
    <span class="divider"></span>
    <ul class="contacts">
      <li><svg viewBox="0 0 24 24"><path d="M6.6 10.8a15 15 0 0 0 6.6 6.6l2.2-2.2c.3-.3.7-.4 1-.2 1.1.4 2.3.6 3.6.6.6 0 1 .4 1 1V20c0 .6-.4 1-1 1A17 17 0 0 1 3 4c0-.6.4-1 1-1h3.5c.6 0 1 .4 1 1 0 1.3.2 2.5.6 3.6.1.3 0 .7-.2 1z"/></svg>(555) 274-8160</li>
      <li><svg viewBox="0 0 24 24"><path d="M2 10l10-7 10 7v11H2zm2 1.2V19h16v-7.8l-8 5.3z"/></svg>pastormorrowbga@example.com</li>
      <li><svg viewBox="0 0 24 24"><path d="M12 2a7 7 0 0 0-7 7c0 5 7 13 7 13s7-8 7-13a7 7 0 0 0-7-7zm0 9.5A2.5 2.5 0 1 1 12 6.5a2.5 2.5 0 0 1 0 5z"/></svg><span>4120 Brambleton Rd.<br>Brambleton Tn. 55501</span></li>
    </ul>
    <div class="web-band">www.Brambleton1stGraceAssembly.example</div>
  </section>

  <section class="card card-cover" aria-label="Folding card cover">
    <p class="center-name">Brambleton<br>Grace Assembly Church</p>
  </section>

  <section class="card card-inside" aria-label="Folding card inside">
    <div class="winter-photo" role="img" aria-label="Soft-focus photo of frosted white winter flowers and grasses with falling snow"></div>
    <p class="thanks">Thank You For Visiting</p>
    <div class="lockup">
      <span class="dot"></span>
      <div><div class="town">Brambleton</div><div class="sub">GRACE ASSEMBLY CHURCH</div></div>
    </div>
  </section>

</body>
</html>
```